Create UX design for an IT company deals in AI/ML based products

Dear Design Creators,

We are looking for an excellent website design for AIML based company. We are creating this contest for creative designers, who are looking for long term association and repeat opportunities to work with us. Only most creative designer understands the power of content placement with an attractive design.

We are not orthodox thus, you are free to create the best design possible for the AIML based company. For reference visit VOLT KESARIYA website. We would love to see the combination of DARK theme. Let's see what can you prepare for us.

Note: Make sure you use the trendy but pro. font families and colors.

Preferred colors - Blue, White and Black

What pages we are looking for?

1. About Us (About Company + Team)
2. Blog
3. Home Page (Animation/Videos)
4. Products
5. Solutions
6. Contact Us
7. Footer

IMP Points to be covered in Home Page

1. Banner, with TECH AIML Video (You can put place Holder)
2. Nice and crisp fonts, buttons
3. Neat and Clean design
4. Most Imp. SYNOPSIS of pages (Service, Products, Blogs) must be covered

NOTE: Selected designer may be awarded with BONUE + ADDITIONAL WORK.

Reference Link:

https://www.voltkesariya.example/

Good Luck

```html
<!DOCTYPE html>
<html lang="en">
<head>
<meta charset="utf-8">
<title>Best It Company</title>
<link rel="stylesheet" href="https://fonts.googleapis.com/css2?family=Poppins:ital,wght@0,300;0,400;0,500;0,600;0,700;1,300;1,400;1,500&display=swap">
<style>
:root{
  --bg:#1b1b1b;
  --bg-soft:#212121;
  --panel:#262626;
  --field:#2c2c2c;
  --cyan:#12aad6;
  --teal:#0b7791;
  --white:#ffffff;
  --muted:#cfcfcf;
}
*{box-sizing:border-box;margin:0;padding:0}
html,body{width:1200px;height:4568px;overflow:hidden}
body{position:relative;background:var(--bg);color:var(--white);font-family:"Poppins",sans-serif}
.abs{position:absolute}
.ph{position:absolute}

/* hero */
.hero{left:0;top:0;width:1200px;height:582px;background:linear-gradient(180deg,#2c3036 0%,#3b4046 45%,#23272b 100%)}
.nav{left:0;top:16px;width:1200px;height:30px}
.nav a{position:absolute;top:0;color:var(--white);text-decoration:none;font-size:18px;font-weight:500}
.nav a.active{border-bottom:2px solid var(--white);padding-bottom:2px}
.hero-title{left:110px;top:232px;font-size:60px;font-weight:700;line-height:1}
.hero-line{left:110px;top:328px;width:60px;height:3px;background:var(--cyan)}
.hero-sub{left:182px;top:315px;font-size:21px;font-style:italic;font-weight:400}
.btn{position:absolute;background:var(--teal);color:var(--white);font-style:italic;font-size:19px;display:flex;align-items:center;justify-content:center;border-radius:2px 12px 2px 2px}

/* about */
.about-left{left:0;top:582px;width:600px;height:531px;background:var(--bg)}
.about-right{left:600px;top:582px;width:600px;height:531px;background:var(--bg-soft)}
.blob-label{font-weight:600;color:var(--white)}
.para{font-size:18px;line-height:28.5px;font-weight:400;color:var(--white)}
.learn{left:23px;top:948px;font-size:20px;font-style:italic}
.learn::after{content:"";position:absolute;left:0;bottom:-4px;width:80px;height:2px;background:var(--cyan)}

/* team */
.team-panel{left:0;top:1113px;width:784px;height:531px;background:var(--teal)}
.team-title{left:119px;top:1240px;font-size:53px;font-weight:600;line-height:85px}
.card{position:absolute;top:1202px;width:213px;height:330px;background:var(--panel);overflow:hidden}
.card .photo{position:absolute;left:0;top:0;width:100%;height:239px}
.card .name{position:absolute;left:0;top:256px;width:100%;text-align:center;font-size:20px;font-weight:500}
.card .role{position:absolute;left:0;top:288px;width:100%;text-align:center;font-size:15px;font-style:italic;color:var(--muted)}
.socials{position:absolute;display:flex;gap:30px}
.socials span{display:block;width:30px;height:30px;background:var(--cyan);border-radius:3px}

/* services */
.svc{position:absolute;width:284px;height:201px;background:var(--panel);text-align:center}
.svc .num{position:absolute;left:0;width:100%;top:-62px;font-size:80px;font-weight:700;font-style:italic;color:#3a3a3a;line-height:1}
.svc h3{margin-top:46px;font-size:24px;font-weight:500}
.svc p{margin:18px auto 0;width:230px;font-size:15px;line-height:24px}
.svc .more{display:block;margin-top:12px;font-size:15px;font-style:italic;color:var(--cyan)}
.svc-title{left:600px;top:1735px;width:503px;text-align:center;font-size:57px;font-weight:600}
.svc-text{left:620px;top:1830px;width:490px;text-align:center;font-size:22px;font-style:italic;line-height:32px}
.see-all-v{left:1150px;top:2010px;transform:rotate(90deg);transform-origin:left top;font-size:22px;font-style:italic;color:var(--cyan);text-decoration:underline;left:1180px}

/* product */
.prod{position:absolute;top:2418px;width:316px;height:387px}
.arrow{position:absolute;top:2585px;width:62px;height:51px;background:var(--white);display:flex;align-items:center;justify-content:center}

/* solutions */
.sol-head{left:0;top:2966px;width:486px;height:85px;background:var(--bg-soft);font-size:48px;font-weight:600;padding:12px 0 0 20px;line-height:60px}
.sol-head .hl{color:var(--cyan)}
.pill{position:absolute;left:44px;width:272px;height:64px;border:2px solid var(--teal);border-radius:12px;display:flex;align-items:center;justify-content:center;font-size:28px;font-style:italic;font-weight:300;color:var(--teal)}
.divider{left:388px;top:3112px;width:1px;height:345px;background:#3a3a3a}
.check{position:absolute;font-size:19px;padding-left:32px}
.check svg{position:absolute;left:0;top:4px}

/* contact */
.field{position:absolute;left:622px;width:534px;background:var(--field);color:#bbbbbb;font-size:19px;padding:0 36px;display:flex;align-items:center}
.info{position:absolute;left:76px;font-size:19px;padding-left:46px}
.info svg{position:absolute;left:0;top:0}

/* footer */
.footer{left:0;top:4326px;width:1200px;height:242px;background:#232323}
.foot-link{position:absolute;font-size:25px;color:var(--white)}
</style>
</head>
<body>

<!-- HERO -->
<div class="ph hero" role="img" aria-label="Dark open-plan office interior photo"></div>
<nav class="abs nav">
  <a class="active" style="left:413px">Home</a>
  <a style="left:514px">About</a>
  <a style="left:615px">Services</a>
  <a style="left:739px">Product</a>
  <a style="left:858px">Solutions</a>
  <a style="left:989px">Contact</a>
  <a style="left:1110px">Blog</a>
</nav>
<h1 class="abs hero-title">Best It Company</h1>
<div class="abs hero-line"></div>
<div class="abs hero-sub">Fresh Ideas For Your Business</div>
<a class="btn" style="left:110px;top:371px;width:138px;height:40px">See More</a>

<!-- ABOUT -->
<div class="abs about-left"></div>
<div class="abs about-right"></div>
<svg class="abs" style="left:0;top:518px" width="241" height="177" viewBox="0 0 241 177">
  <path d="M70 8 C120 -6 200 6 230 40 C250 70 236 130 200 155 C160 182 100 180 62 160 C30 145 0 120 2 95 C4 70 30 65 38 45 C46 25 50 14 70 8Z" fill="var(--cyan)"/>
</svg>
<div class="abs blob-label" style="left:57px;top:570px;font-size:42px">About</div>
<p class="abs para" style="left:23px;top:734px;width:360px">Lorem ipsum dolor sit amet, consea dipiscing elit ut aliquam, purus sit amet luctus venenatis, lectus magna fringilla urna, porttitor rhoncus ectus magna fringilla urna, porttitor rhoncus</p>
<a class="abs learn">Learn More</a>
<div class="ph" style="left:406px;top:695px;width:378px;height:307px;background:linear-gradient(180deg,#4d5257,#8b9196 55%,#5d6266)" role="img" aria-label="Bright modern office with long desks"></div>
<p class="abs para" style="left:808px;top:734px;width:370px">Lorem ipsum dolor sit amet, consectetur adipiscing elit ut aliquam, purus sit amet luctus venenatis, lectus magna fringilla urna, porttitor rhoncus</p>
<p class="abs para" style="left:808px;top:857px;width:370px">Lorem ipsum dolor sit amet, consectetur adipiscing elit ut aliquam, purus sit amet luctus venenatis, lectus magna fringilla urna, porttitor rhoncus</p>

<!-- TEAM -->
<div class="abs team-panel"></div>
<h2 class="abs team-title">Our<br>Team</h2>
<svg class="abs" style="left:140px;top:1428px" width="100" height="44" viewBox="0 0 100 44">
  <circle cx="23" cy="22" r="20" fill="none" stroke="#fff" stroke-width="2.5"/>
  <path d="M27 14 L19 22 L27 30" fill="none" stroke="#fff" stroke-width="3"/>
  <circle cx="76" cy="22" r="20" fill="none" stroke="#fff" stroke-width="2.5"/>
  <path d="M72 14 L80 22 L72 30" fill="none" stroke="#fff" stroke-width="3"/>
</svg>
<div class="card" style="left:370px"><div class="photo" role="img" aria-label="Portrait of team member" style="background:linear-gradient(180deg,#5a5a5a,#2e2e2e)"></div><div class="name">Ravi Nolan</div><div class="role">Founder</div></div>
<div class="card" style="left:613px"><div class="photo" role="img" aria-label="Portrait of team member" style="background:linear-gradient(180deg,#d8dde0,#6f8894 60%,#0b7791)"></div>
  <div class="socials" style="left:30px;top:269px"><span aria-label="social link"></span><span aria-label="social link"></span><span aria-label="social link"></span></div></div>
<div class="card" style="left:856px"><div class="photo" role="img" aria-label="Portrait of team member" style="background:linear-gradient(180deg,#cfcfcf,#4a4a4a)"></div><div class="name">Ravi Nolan</div><div class="role">Founder</div></div>
<div class="card" style="left:1099px"><div class="photo" role="img" aria-label="Portrait of team member" style="background:linear-gradient(180deg,#3d3d3d,#1f1f1f)"></div><div class="name" style="text-align:left;padding-left:42px;width:300px">Ravi Nolan</div><div class="role" style="text-align:left;padding-left:54px;width:300px">Founder</div></div>

<!-- SERVICES -->
<div class="svc" style="left:0;top:1752px"><div class="num">01</div><h3>Service title</h3><p>Lorem ipsum dolor sit amet, consectetur adipiscing</p><span class="more">More</span></div>
<div class="ph" style="left:284px;top:1752px;width:283px;height:200px;background:linear-gradient(135deg,#1d2a44,#0f1526 60%,#27324a)" role="img" aria-label="Code on a laptop screen"></div>
<div class="ph" style="left:0;top:1952px;width:284px;height:202px;background:linear-gradient(135deg,#e6e6e6,#a9a9a9 50%,#2c2c2c)" role="img" aria-label="Laptop on a white desk"></div>
<div class="svc" style="left:284px;top:1952px"><div class="num">02</div><h3>Service title</h3><p>Lorem ipsum dolor sit amet, consectetur adipiscing</p><span class="more">More</span></div>
<div class="ph" style="left:567px;top:1952px;width:284px;height:202px;background:linear-gradient(135deg,#f2f2f2,#cfcfcf 60%,#9f9f9f)" role="img" aria-label="Robotic hand on white background"></div>
<div class="svc" style="left:851px;top:1952px"><div class="num">03</div><h3>Service title</h3><p>Lorem ipsum dolor sit amet, consectetur adipiscing</p><span class="more">More</span></div>
<h2 class="abs svc-title">Our Services</h2>
<p class="abs svc-text">Lorem ipsum dolor sit amet, consectetur adipiscing elit ut aliquam, purus sit amet luctus venenatis</p>
<div class="abs see-all-v">See All</div>

<!-- PRODUCT -->
<svg class="abs" style="left:466px;top:2225px" width="142" height="119" viewBox="0 0 142 119">
  <path d="M40 4 C80 -4 130 6 139 40 C146 78 120 116 80 118 C44 120 28 96 8 86 C-6 76 2 50 14 32 C22 18 26 8 40 4Z" fill="var(--cyan)"/>
</svg>
<h2 class="abs" style="left:530px;top:2254px;font-size:46px;font-weight:600">Product</h2>
<div class="prod" style="left:106px;background:radial-gradient(circle at 50% 45%,#1b2c9a,#05061a 70%)" role="img" aria-label="Blue light trail"></div>
<div class="prod" style="left:441px;background:linear-gradient(180deg,#0b3fbf,#0a5bd8 60%,#0838a0)" role="img" aria-label="Glass prism on blue"></div>
<div class="prod" style="left:777px;background:radial-gradient(circle at 50% 50%,#1b3a55,#08111c 75%)" role="img" aria-label="Network of glowing cubes"></div>
<div class="arrow" style="left:60px"><svg width="20" height="20" viewBox="0 0 20 20"><path d="M14 3 L6 10 L14 17" fill="none" stroke="var(--cyan)" stroke-width="4"/></svg></div>
<div class="arrow" style="left:1067px"><svg width="20" height="20" viewBox="0 0 20 20"><path d="M6 3 L14 10 L6 17" fill="none" stroke="var(--cyan)" stroke-width="4"/></svg></div>
<a class="btn" style="left:525px;top:2853px;width:150px;height:48px;background:var(--cyan);font-size:24px">See All</a>

<!-- SOLUTIONS -->
<h2 class="abs sol-head"><span class="hl">Creative</span> Solutions</h2>
<div class="pill" style="top:3129px">Ai Solutions</div>
<div class="pill" style="top:3237px">ML Solutions</div>
<div class="pill" style="top:3346px">Tech Solutions</div>
<div class="abs divider"></div>
<svg class="abs" style="left:389px;top:3150px" width="12" height="18"><path d="M0 0 L12 9 L0 18Z" fill="#3a3a3a"/></svg>
<p class="abs" style="left:441px;top:3140px;width:720px;font-size:21px;line-height:32px">Lorem ipsum dolor sit amet, consectetur adipiscing elit ut aliquam, purus sit amet luctus venenatis, lectus magna fringilla urna, porttitor rhoncus dolor purus non enim praesent elementum facilisis leo.</p>
<div class="check" style="left:441px;top:3316px"><svg width="20" height="16"><path d="M2 8 L8 14 L18 2" fill="none" stroke="var(--cyan)" stroke-width="3"/></svg>Lorem ipsum dolor sit amet</div>
<div class="check" style="left:441px;top:3357px"><svg width="20" height="16"><path d="M2 8 L8 14 L18 2" fill="none" stroke="var(--cyan)" stroke-width="3"/></svg>Lorem ipsum dolor sit amet</div>
<div class="check" style="left:441px;top:3399px"><svg width="20" height="16"><path d="M2 8 L8 14 L18 2" fill="none" stroke="var(--cyan)" stroke-width="3"/></svg>Lorem ipsum dolor sit amet</div>
<div class="check" style="left:830px;top:3316px"><svg width="20" height="16"><path d="M2 8 L8 14 L18 2" fill="none" stroke="var(--cyan)" stroke-width="3"/></svg>Lorem ipsum dolor sit amet</div>
<div class="check" style="left:830px;top:3357px"><svg width="20" height="16"><path d="M2 8 L8 14 L18 2" fill="none" stroke="var(--cyan)" stroke-width="3"/></svg>Lorem ipsum dolor sit amet</div>
<div class="check" style="left:830px;top:3399px"><svg width="20" height="16"><path d="M2 8 L8 14 L18 2" fill="none" stroke="var(--cyan)" stroke-width="3"/></svg>Lorem ipsum dolor sit amet</div>

<!-- CONTACT -->
<svg class="abs" style="left:44px;top:3525px" width="296" height="195" viewBox="0 0 296 195">
  <path d="M60 20 C100 -4 190 -2 240 20 C290 44 300 110 270 150 C240 190 170 198 120 186 C70 174 20 160 6 120 C-6 80 24 42 60 20Z" fill="var(--cyan)"/>
</svg>
<div class="abs" style="left:128px;top:3592px;font-size:19px;color:#1b1b1b">Let's Talk !</div>
<h2 class="abs" style="left:121px;top:3610px;font-size:53px;font-weight:600">Contact Us</h2>
<p class="abs" style="left:76px;top:3758px;width:500px;font-size:21px;font-weight:600;line-height:32px">Lorem ipsum dolor sit amet, consectetur adipiscing elit ut aliquam, purus sit amet luctus venenatis, lectus magna fringilla urna, porttitor</p>
<div class="info" style="top:3932px"><svg width="24" height="24" viewBox="0 0 24 24"><path d="M5 2 L9 2 L11 7 L8 9 C9.5 12 12 14.5 15 16 L17 13 L22 15 L22 19 C22 21 20 22 18 22 C9 21 3 15 2 6 C2 4 3 2 5 2Z" fill="var(--cyan)"/></svg>+(XX) XXX XXX</div>
<div class="info" style="top:3986px"><svg width="22" height="26" viewBox="0 0 22 26"><path d="M11 1 C5 1 1 5 1 10 C1 17 11 25 11 25 C11 25 21 17 21 10 C21 5 17 1 11 1Z" fill="var(--cyan)"/><circle cx="11" cy="10" r="4" fill="#1b1b1b"/></svg>Lorem ipsum dolor sit amet, consectetur</div>
<div class="socials" style="left:205px;top:4077px"><span aria-label="social link"></span><span aria-label="social link"></span><span aria-label="social link"></span></div>

<div class="field" style="top:3590px;height:64px">Your Name</div>
<div class="field" style="top:3699px;height:65px">Subject</div>
<div class="field" style="top:3807px;height:65px">Your Email</div>
<div class="field" style="top:3915px;height:216px;align-items:flex-start;padding-top:22px">Message</div>
<a class="btn" style="left:622px;top:4179px;width:151px;height:46px;background:var(--cyan);font-style:normal;font-weight:600;font-size:21px">Send</a>

<!-- FOOTER -->
<footer class="abs footer">
  <h2 class="abs" style="left:87px;top:20px;font-size:44px;font-weight:600">Explore</h2>
  <a class="foot-link" style="left:87px;top:80px">Home</a>
  <a class="foot-link" style="left:238px;top:80px">Services</a>
  <a class="foot-link" style="left:388px;top:80px">Blog</a>
  <a class="foot-link" style="left:87px;top:128px">Portfolio</a>
  <a class="foot-link" style="left:238px;top:128px">Contact</a>
  <a class="foot-link" style="left:87px;top:176px">About</a>
  <a class="foot-link" style="left:236px;top:180px">Solutions</a>
  <h3 class="abs" style="left:622px;top:90px;font-size:34px;font-weight:600">Social Media</h3>
  <div class="socials" style="left:958px;top:100px"><span aria-label="social link"></span><span aria-label="social link"></span><span aria-label="social link"></span></div>
</footer>

</body>
</html>
```